Fizz Bop Lantern Series 1 Volume 1

I am looking for someone to make me a book cover, I want something catchy but classy.

The title of the book is; Fizz Bop Lantern
Series 1 Volume 1

Colors should be: Red, White, Black and Grey

```html
<!DOCTYPE html>
<html lang="en">
<head>
<meta charset="utf-8">
<title>Fizz Bop Lantern — Series 1 Volume 1</title>
<link rel="stylesheet" href="https://fonts.googleapis.com/css2?family=Bebas+Neue&family=Oswald:wght@500;600&family=Roboto:wght@500;700&display=swap">
<style>
  :root {
    --backdrop: #2b2b2b;
    --paper: #ffffff;
    --ink: #333333;
    --red: #e8252b;
    --yellow: #f5c531;
    --grey-light: #ededed;
    --grey-mid: #c9c9c9;
  }
  * { box-sizing: border-box; margin: 0; padding: 0; }
  html, body {
    width: 1200px;
    height: 800px;
    overflow: hidden;
    background: var(--backdrop);
  }
  .canvas {
    position: relative;
    width: 1200px;
    height: 800px;
  }
  .cover {
    position: absolute;
    left: 346px;
    top: 30px;
    width: 508px;
    height: 740px;
    background: var(--paper);
    display: flex;
    flex-direction: column;
    align-items: center;
  }
  .volume-tag {
    margin-top: 30px;
    width: 262px;
    height: 40px;
    border: 3px solid var(--red);
    display: flex;
    align-items: center;
    justify-content: center;
    font-family: "Roboto", sans-serif;
    font-weight: 500;
    font-size: 22px;
    letter-spacing: 0.55em;
    padding-left: 0.55em;
    color: var(--ink);
  }
  .title {
    margin-top: 10px;
    text-align: center;
    font-family: "Bebas Neue", "Oswald", sans-serif;
    font-weight: 400;
    line-height: 0.92;
  }
  .title-top {
    display: block;
    font-size: 104px;
    letter-spacing: 0.04em;
    color: var(--ink);
  }
  .title-bottom {
    display: block;
    font-size: 112px;
    letter-spacing: 0.05em;
    color: var(--red);
  }
  .series-tag {
    margin-top: 8px;
    width: 240px;
    height: 38px;
    background: var(--yellow);
    display: flex;
    align-items: center;
    justify-content: center;
    font-family: "Roboto", sans-serif;
    font-weight: 700;
    font-size: 21px;
    letter-spacing: 0.4em;
    padding-left: 0.4em;
    color: var(--ink);
  }
  .artwork {
    margin-top: 18px;
    width: 430px;
    height: 318px;
    background: radial-gradient(ellipse at 50% 45%, #f6d87a 0%, #e6e6e6 35%, #bdbdbd 70%, #ffffff 100%);
  }
  .author-band {
    position: absolute;
    left: 0;
    bottom: 24px;
    width: 100%;
    height: 40px;
    background: var(--red);
    display: flex;
    align-items: center;
    justify-content: center;
    font-family: "Oswald", sans-serif;
    font-weight: 500;
    font-size: 20px;
    letter-spacing: 0.22em;
    color: var(--paper);
    text-transform: uppercase;
  }
</style>
</head>
<body>
  <main class="canvas">
    <section class="cover">
      <div class="volume-tag">VOLUME-1</div>
      <h1 class="title">
        <span class="title-top">FIZZ BOP</span>
        <span class="title-bottom">LANTERN</span>
      </h1>
      <div class="series-tag">SERIES-1</div>
      <div class="artwork" role="img" aria-label="Illustration of a yellow folder linked by cables to four black file drives"></div>
      <div class="author-band">Marla Jean Tillet</div>
    </section>
  </main>
</body>
</html>
```